Tamarind Crest Management - Business Cards

I need business cards. My current logo was designed by a designer at this site and I very much like and am happy with the results. I would like a business card that is trendy, unique, current yet professional. I deal with high net worth clients daily

Target Market(s)

Out of state investors looking to get into the rental market in Ohio

Industry/Entity Type

Property Management, Consulting

Contact Information for Business Card

Name, Title (Chief Financial Officer) office phone number (347) 681-9072 website address tamcrestmgmt.example

Font styles to use
Sans Serif

Colors
0054AA
0677BA
7BADD7
CADEEF
E8F1F8
0094D4
00A9DD
6FCCEA
C7EBF8
E9F6FB
00AB8E
00BBA5
67D7C9
C6EFE9
E9F9F6

```html
<!DOCTYPE html>
<html lang="en">
<head>
<meta charset="utf-8">
<title>Tamarind Crest Management – Business Card</title>
<link href="https://fonts.googleapis.com/css2?family=Work+Sans:wght@400;600;700&display=swap" rel="stylesheet">
<style>
  :root {
    --backdrop: #d9d3cb;
    --card-frost: #ebe6df;
    --card-edge: #f6f3ee;
    --navy: #1f3a63;
    --ink: #1c2a44;
    --ink-soft: #2b2f38;
    --panel-text: #f1ece4;
    --accent-red: #c3282d;
  }
  * { box-sizing: border-box; margin: 0; padding: 0; }
  html, body {
    width: 1200px;
    height: 1047px;
    overflow: hidden;
    background: var(--backdrop);
    font-family: "Work Sans", Arial, sans-serif;
  }
  .stage {
    position: relative;
    width: 1200px;
    height: 1047px;
  }
  .business-card {
    position: absolute;
    left: 125px;
    top: 263px;
    width: 950px;
    height: 520px;
    border-radius: 26px;
    background: var(--card-frost);
    border: 2px solid var(--card-edge);
    overflow: hidden;
    box-shadow: 0 18px 40px rgba(40, 30, 20, 0.18);
  }
  .brand-panel {
    position: absolute;
    left: 0;
    top: 0;
    width: 265px;
    height: 100%;
    background: var(--navy);
  }
  .brand-lockup {
    position: absolute;
    left: 40px;
    top: 150px;
    width: 200px;
    display: flex;
    flex-direction: column;
    gap: 18px;
  }
  .brand-mark {
    width: 34px;
    height: 34px;
    background: var(--accent-red);
  }
  .brand-name {
    color: var(--panel-text);
    font-weight: 700;
    font-size: 34px;
    line-height: 1.12;
    letter-spacing: 0.5px;
  }
  .contact-block {
    position: absolute;
    left: 617px;
    top: 168px;
    width: 333px;
  }
  .person-name {
    color: var(--ink);
    font-weight: 700;
    font-size: 37px;
    letter-spacing: 1.5px;
    line-height: 1.1;
  }
  .person-title {
    margin-top: 12px;
    color: var(--ink-soft);
    font-size: 23px;
    letter-spacing: 0.6px;
  }
  .divider {
    margin-top: 26px;
    width: 333px;
    height: 3px;
    background: var(--ink);
  }
  .contact-line {
    color: var(--ink-soft);
    font-size: 24px;
    letter-spacing: 0.6px;
    line-height: 1.55;
  }
  .contact-list { margin-top: 22px; }
</style>
</head>
<body>
  <main class="stage">
    <section class="business-card" aria-label="Business card for Tamarind Crest Management">
      <div class="brand-panel">
        <div class="brand-lockup">
          <div class="brand-mark" aria-hidden="true"></div>
          <p class="brand-name">Tamarind Crest Management</p>
        </div>
      </div>
      <div class="contact-block">
        <h1 class="person-name">NAME, TITLE</h1>
        <p class="person-title">Chief Financial Officer</p>
        <div class="divider" aria-hidden="true"></div>
        <div class="contact-list">
          <p class="contact-line">(347) 681-9072</p>
          <p class="contact-line">tamcrestmgmt.example</p>
        </div>
      </div>
    </section>
  </main>
</body>
</html>
```